website design for small business consultancy - strategic research and writing

About the business
I am starting a new consultancy business called "Crest Drafting Partners". I have asked for logo designs through Sketch Forum and am in the process of finalising these. I have a professional background and am an excellent and passionate writer and I want this professionalism conveyed through a modern, strong (confident) but simple, professional and elegant website. For SEO purposes, the services I will offer will include, but not be limited to, grants, submissions, proposals, strategic documents, complex correspondence, curriculum vitae and resumes, business cases, reports, training (grants and report writing). I will be based in Perth, Western Australia.

I would prefer the website be presented in black and white but I am not averse to colour, provided it's not gaudy. I want a header band across the top with the capacity to insert my logo (which I will send to the successful web builder) and the nature of the services "Strategic Research and Writing Services". I also want a meet up icon and a contact us button to the right (in the header).

I want a level one menu item underneath the header with the following menus - About (homepage), Services, Testimonials, and Contact (page to include a contact form).

I would like the following text to appear on the homepage as a highlight - like a drawcard for visitors to the site about my passion for what I do - "Harnessing the power of the written word".

I want the capacity for a photo of me to be inserted on the About page.

I would like testimonials to feature distinctly, possibly in a box type format, either horizontally across the page or a couple or few in a row. There needs to be clear delineation of the person providing the testimonial and the testimonial itself.

Generally though I want a one column website that is accessible to those with disabilities. This is important to me as I believe all people should have access to website data.

I want the website to be responsive to tablets and mobile devices with high level SEO. One that is easy to add page headings to, and easy to amend and add plug ins. Maybe a wordpress site? The website must be compatible with Blue Kettle Hosting as I have paid for that.

Use of imagery is fine provided it is open source and relevant to the focus of the business.

Happy to send through further detail if required.

Thank you in anticipation. I have appreciated the work submitted to date.

I will insert the content (yet to be drafted)

Target Market(s)

Local government, private business, government

Contact Information for Business Card

Business card - I would like the logo on the front along with Strategic Research and Writing Services. I want the contact details on the back including: my name, role, email, mobile, web address, address.

I wouldn't mind a side panel on the rear in the colour of the business card with "Harnessing the power of the written word" on it. Maybe with the text going up vertically. I can get the logo in black and white. I will upload the logo asap.

Coding

Number of Pages Required

Font styles to use
Serif
Sans Serif
Script

Requirements
Must have
• I want an elegant business card, professional but modern, that accords in branding to the website.
Should not have
• I do not want to use the red and black logo thanks. Either of the others is fine.

```html
<!DOCTYPE html>
<html lang="en">
<head>
<meta charset="utf-8">
<title>Crest Drafting Partners — Strategic Research and Writing</title>
<link rel="stylesheet" href="https://fonts.googleapis.com/css2?family=Libre+Baskerville:wght@400;700&family=Lato:wght@400;700&display=swap">
<style>
:root{
  --red:#e31e24;
  --ink:#222222;
  --muted:#555555;
  --light:#f6f6f6;
  --card:#f1f1f1;
  --line:#d6d6d6;
  --footer:#1f1f1f;
  --white:#ffffff;
  --serif:'Libre Baskerville', Georgia, serif;
  --sans:'Lato', Arial, sans-serif;
}
*{box-sizing:border-box;margin:0;padding:0}
html,body{width:1200px;height:4000px;overflow:hidden;background:var(--white)}
body{position:relative;font-family:var(--sans);color:var(--ink)}
.abs{position:absolute}
.btn{position:absolute;display:flex;align-items:center;justify-content:center;background:var(--red);color:var(--white);font-family:var(--sans);font-size:14px;border-radius:22px;text-decoration:none}
.serif{font-family:var(--serif)}

/* header */
.site-header{position:absolute;left:0;top:0;width:1200px;height:101px;background:var(--white)}
.brand{position:absolute;left:75px;top:36px;font-family:var(--serif);font-size:21px;font-weight:700;color:var(--ink);display:flex;align-items:center;gap:10px}
.brand-square{width:26px;height:26px;border:2px solid var(--ink)}
.main-nav{position:absolute;top:46px;left:0;font-family:var(--serif);font-size:12.5px;color:#444}
.main-nav a{position:absolute;white-space:nowrap;color:#444;text-decoration:none}
.main-nav a.active{color:var(--ink);font-weight:700;border-bottom:2px solid var(--ink);padding-bottom:6px}
.call{position:absolute;left:975px;top:36px;display:flex;gap:8px;align-items:center}
.call small{display:block;color:var(--red);font-size:11px;font-weight:700}
.call strong{display:block;font-size:12px;font-weight:700;color:var(--ink)}

/* hero */
.hero{position:absolute;left:0;top:101px;width:1200px;height:512px;background:linear-gradient(100deg,#5f5c58 0%,#8b847c 45%,#c8beb3 75%,#a69a8e 100%)}
.hero-frame{position:absolute;left:208px;top:124px;width:331px;height:241px;border:2px solid rgba(255,255,255,.85)}
.hero h1{position:absolute;left:121px;top:174px;font-family:var(--serif);font-weight:700;font-size:29px;line-height:39px;letter-spacing:2px;color:var(--white)}
.hero .hero-btn{position:absolute;left:124px;top:267px;width:171px;height:46px;background:#f2f2f2;color:#444;font-family:var(--serif);font-weight:700;font-size:12px;display:flex;align-items:center;justify-content:center}
.dots{position:absolute;display:flex;gap:7px}
.dots span{width:8px;height:8px;border-radius:50%;background:#cfcfcf}
.dots span.on{background:var(--red)}

/* about */
.about-title{position:absolute;left:84px;top:730px;font-family:var(--serif);font-size:28px;font-weight:700}
.about-title::after{content:"";position:absolute;left:0;top:46px;width:128px;height:2px;background:var(--red)}
.about-text{position:absolute;left:80px;width:500px;font-size:13px;line-height:16px;color:#333}
.photo{position:absolute}

/* services */
.section-title{position:absolute;left:0;width:1200px;text-align:center;font-family:var(--serif);font-size:30px;font-weight:700}
.service-card{position:absolute;top:1163px;width:495px;height:482px;background:var(--light)}
.service-card .photo{left:0;top:0;width:495px;height:290px}
.service-icon{position:absolute;left:216px;top:250px;width:62px;height:62px;border-radius:50%;background:var(--white);display:flex;align-items:center;justify-content:center}
.service-card h3{position:absolute;left:0;width:495px;text-align:center;font-family:var(--serif);font-size:21px;font-weight:700}
.service-card p{position:absolute;left:22px;width:460px;font-size:13px;line-height:17px;color:#444}

/* consultancy band */
.consult{position:absolute;left:0;top:1726px;width:1200px;height:450px;background:linear-gradient(110deg,#2f3237 0%,#4b4f55 40%,#7b7f85 70%,#56595e 100%)}
.consult-frame{position:absolute;left:267px;top:105px;width:358px;height:295px;border:2px solid rgba(255,255,255,.8)}
.consult h2{position:absolute;left:200px;top:158px;font-family:var(--serif);font-weight:700;font-size:32px;line-height:44px;color:var(--white);letter-spacing:1px}
.consult p{position:absolute;left:206px;top:250px;width:400px;font-size:13px;line-height:16px;color:var(--white)}

/* capabilities */
.capability{position:absolute;width:240px;text-align:center;font-family:var(--serif);font-size:21px;line-height:28px;color:#333}
.capability svg{display:block;margin:0 auto}

/* testimonials */
.testimonial{position:absolute;top:2845px;width:327px;height:327px;background:var(--card);text-align:center}
.avatar{position:absolute;left:115px;top:29px;width:96px;height:96px;border-radius:50%;background:linear-gradient(135deg,#3d6f9a,#d9b799)}
.testimonial .name{position:absolute;left:0;top:145px;width:327px;font-family:var(--serif);font-size:16px}
.testimonial .role{position:absolute;left:0;top:170px;width:327px;font-size:13px;color:#666}
.testimonial .quote{position:absolute;left:26px;top:195px;width:275px;font-size:12.5px;line-height:16px;color:#333}
.stars{position:absolute;left:0;top:250px;width:327px;color:#f2a516;font-size:14px;letter-spacing:4px}
.feature-photo{position:absolute;left:793px;top:2845px;width:326px;height:327px;background:linear-gradient(180deg,#cfe0ef 0%,#eef3f8 50%,#7a9a5d 100%)}
.feature-photo p{position:absolute;left:26px;top:86px;font-family:var(--serif);font-size:22px;line-height:24px;color:#222;letter-spacing:1px}

/* contact */
.field{position:absolute;border:1px solid var(--line);background:var(--white);font-size:13px;color:#555;padding:0 14px;display:flex;align-items:center}
.field.message{align-items:flex-start;padding-top:12px}

/* footer */
.site-footer{position:absolute;left:0;top:3610px;width:1200px;height:317px;background:var(--footer);color:var(--white)}
.site-footer h4{position:absolute;font-family:var(--serif);font-size:17px;font-weight:700}
.site-footer h4::after{content:"";position:absolute;left:0;top:28px;width:40px;height:2px;background:var(--red)}
.site-footer .txt{position:absolute;font-size:13px;line-height:17px}
.quick-links{position:absolute;left:390px;top:130px;list-style:none;font-size:13px}
.quick-links li{height:24.2px;position:relative;padding-left:18px}
.quick-links li::before{content:"";position:absolute;left:0;top:6px;width:5px;height:5px;border-radius:50%;background:var(--white)}
.contact-row{position:absolute;left:578px;display:flex;gap:12px;font-size:13px;align-items:center}
.contact-row svg{width:14px;height:14px;flex:none}
.news-input{position:absolute;left:835px;top:158px;width:284px;height:36px;border-radius:18px;background:var(--white);color:#777;font-size:13px;padding-left:20px;display:flex;align-items:center}
.copyright{position:absolute;left:85px;top:3954px;font-size:13px;color:#333}
.social{position:absolute;top:3949px;width:26px;height:26px;border-radius:50%;background:#222}
.social.red{background:var(--red)}
</style>
</head>
<body>

<header class="site-header">
  <div class="brand"><span class="brand-square"></span>Crest Drafting Partners</div>
  <nav class="main-nav">
    <a class="active" href="#" style="left:520px">Home</a>
    <a href="#" style="left:587px">About Us</a>
    <a href="#" style="left:675px">Services</a>
    <a href="#" style="left:757px">Testimonials</a>
    <a href="#" style="left:864px">Contact Us</a>
  </nav>
  <div class="call">
    <svg width="26" height="26" viewBox="0 0 26 26" aria-hidden="true"><circle cx="13" cy="13" r="11.5" fill="none" stroke="#e31e24" stroke-width="1.6"/><path d="M9 7.5l2.2 2.6-1.3 1.8c.8 1.6 2 2.8 3.6 3.6l1.8-1.3 2.6 2.2-1.5 1.9c-4.2-.4-8.3-4.5-8.7-8.7z" fill="none" stroke="#e31e24" stroke-width="1.4" stroke-linejoin="round"/></svg>
    <div><small>Call Us Now</small><strong>(00)-987-654-321</strong></div>
  </div>
</header>

<section class="hero">
  <div class="abs" style="inset:0" role="img" aria-label="Close-up photograph of a hand writing in a notebook with a red pen"></div>
  <div class="hero-frame"></div>
  <h1>Harnessing The Power of<br>The Written Word</h1>
  <a class="hero-btn" href="#">Read More</a>
  <svg class="abs" style="left:28px;top:232px" width="18" height="30" viewBox="0 0 18 30" aria-hidden="true"><path d="M15 3L4 15l11 12" fill="none" stroke="#d8d8d8" stroke-width="3"/></svg>
  <svg class="abs" style="left:1148px;top:232px" width="18" height="30" viewBox="0 0 18 30" aria-hidden="true"><path d="M3 3l11 12L3 27" fill="none" stroke="#d8d8d8" stroke-width="3"/></svg>
  <div class="dots" style="left:575px;top:475px"><span class="on"></span><span></span><span></span><span></span></div>
</section>

<section class="about">
  <h2 class="about-title">About us</h2>
  <p class="about-text" style="top:815px">Lorem Ipsum is simply dummy text the printing and typesetting industry Ipsum has been the industry's standard dummy text ever since the 1500s,</p>
  <p class="about-text" style="top:866px">when an unknown printer took a galley of type and scrambled it to make a type specimen book. It has survived not only five a centuries, but also in the leap into electronic typesetting, remaining essentially unchanged</p>
  <a class="btn" href="#" style="left:79px;top:944px;width:157px;height:40px">Read More</a>
  <div class="photo" style="left:622px;top:684px;width:496px;height:332px;background:linear-gradient(90deg,#d9dcd8 0%,#eef0ee 45%,#c4c2bd 80%,#8d8780 100%)" role="img" aria-label="Photograph of two people working at computers in a bright office"></div>
</section>

<h2 class="section-title" style="top:1086px">Our Services</h2>

<article class="service-card" style="left:81px">
  <div class="photo" style="background:linear-gradient(135deg,#6c7072 0%,#b9b3a3 50%,#585c60 100%)" role="img" aria-label="Photograph of a team reviewing charts and sticky notes on a table"></div>
  <div class="service-icon">
    <svg width="30" height="30" viewBox="0 0 30 30" aria-hidden="true" fill="none" stroke="#333" stroke-width="1.4"><rect x="9" y="5" width="16" height="21"/><path d="M13 18h8M13 21h8M17 14h4"/><circle cx="9" cy="11" r="4"/><path d="M6 14l-3 4"/></svg>
  </div>
  <h3 style="top:318px">Strategic Research</h3>
  <p style="top:355px">Lorem Ipsum is simply dummy text the printing and typesetting industry has been the industry's standard dummy text ever since the 1500s</p>
  <a class="btn" href="#" style="left:169px;top:415px;width:157px;height:39px">Read More</a>
</article>

<article class="service-card" style="left:622px">
  <div class="photo" style="background:linear-gradient(135deg,#3d3f42 0%,#6e6a66 45%,#5a3a28 80%,#2f2f31 100%)" role="img" aria-label="Photograph of a person writing at a wooden desk"></div>
  <div class="service-icon">
    <svg width="30" height="30" viewBox="0 0 30 30" aria-hidden="true" fill="none" stroke="#333" stroke-width="1.4"><rect x="5" y="5" width="17" height="21"/><path d="M9 11h9M9 15h6M9 19h5"/><path d="M14 22l11-11 2 2-11 11-3 1z"/></svg>
  </div>
  <h3 style="top:314px">Writing Services</h3>
  <p style="top:355px">Lorem Ipsum is simply dummy text the printing and typesetting industry has been the industry's standard dummy text ever since the 1500s</p>
  <a class="btn" href="#" style="left:169px;top:415px;width:157px;height:39px">Read More</a>
</article>

<section class="consult">
  <div class="abs" style="inset:0" role="img" aria-label="Photograph of two business people signing a document"></div>
  <div class="consult-frame"></div>
  <h2>Professional Business<br>Consultancy</h2>
  <p>Lorem Ipsum is simply dummy text the printing and typesetting industryhas been the industry's standard dummy text ever since the 1500s</p>
  <a class="btn" href="#" style="left:205px;top:310px;width:157px;height:38px">Read More</a>
</section>

<section class="capabilities">
  <div class="capability" style="left:117px;top:2289px">
    <svg width="62" height="78" viewBox="0 0 62 78" aria-hidden="true" fill="none" stroke="#e31e24" stroke-width="2.4"><rect x="8" y="4" width="44" height="68"/><path d="M14 12h16M14 24h32M14 32h32M14 40h22M24 58l22-22 4 4-22 22-6 2z"/></svg>
    <div style="margin-top:22px">Grants</div>
  </div>
  <div class="capability" style="left:364px;top:2289px">
    <svg width="72" height="78" viewBox="0 0 72 78" aria-hidden="true" fill="none" stroke="#e31e24" stroke-width="2.4"><path d="M8 4h34l10 10v20M8 4v68h28"/><path d="M16 20h20M16 30h26M16 40h16M16 50h14"/><circle cx="52" cy="56" r="15"/><path d="M52 64V49M45 55l7-7 7 7"/></svg>
    <div style="margin-top:22px">Submissions</div>
  </div>
  <div class="capability" style="left:591px;top:2289px">
    <svg width="78" height="78" viewBox="0 0 78 78" aria-hidden="true" fill="none" stroke="#e31e24" stroke-width="2.4"><path d="M44 10H10v64h44V40"/><path d="M26 50l30-38 8 7-30 38-10 3zM18 64h28"/></svg>
    <div style="margin-top:22px">Proposals</div>
  </div>
  <div class="capability" style="left:821px;top:2289px">
    <svg width="100" height="78" viewBox="0 0 100 78" aria-hidden="true" fill="none" stroke="#e31e24" stroke-width="2.4"><rect x="38" y="4" width="58" height="46"/><rect x="4" y="24" width="58" height="46"/><path d="M12 40h22M12 48h16M48 38h8M70 18h18M70 26h18M46 14h14"/><circle cx="24" cy="60" r="4"/><path d="M32 66l18-20 4 4-18 20z"/></svg>
    <div style="margin-top:22px">Business Cases</div>
  </div>

  <div class="capability" style="left:113px;top:2468px">
    <svg width="72" height="76" viewBox="0 0 72 76" aria-hidden="true" fill="none" stroke="#e31e24" stroke-width="2.4"><path d="M14 4h36v40M14 4v30"/><path d="M20 14h24M20 22h24M20 30h18"/><path d="M4 36l32 20 32-20v36H4zM4 72l24-18M68 72L44 54"/><path d="M34 58l24-30 5 4-24 30"/></svg>
    <div style="margin-top:22px">Complex<br>Correspondence</div>
  </div>
  <div class="capability" style="left:358px;top:2468px">
    <svg width="62" height="78" viewBox="0 0 62 78" aria-hidden="true" fill="none" stroke="#e31e24" stroke-width="2.4"><rect x="4" y="10" width="54" height="66"/><rect x="20" y="4" width="22" height="10"/><circle cx="31" cy="28" r="7"/><path d="M19 44c2-6 22-6 24 0M14 52h34M14 60h34M14 68h34"/></svg>
    <div style="margin-top:22px">Curriculum<br>Vitae and Resumes</div>
  </div>
  <div class="capability" style="left:586px;top:2468px">
    <svg width="72" height="76" viewBox="0 0 72 76" aria-hidden="true" fill="none" stroke="#e31e24" stroke-width="2.4"><path d="M8 4h40l10 10v20M8 4v56h30"/><circle cx="30" cy="26" r="13"/><circle cx="30" cy="26" r="6"/><path d="M30 26l12-12M40 56l20-24 5 5-20 24-7 2z"/></svg>
    <div style="margin-top:22px">Strategic<br>Documents</div>
  </div>
  <div class="capability" style="left:811px;top:2468px">
    <svg width="90" height="76" viewBox="0 0 90 76" aria-hidden="true" fill="none" stroke="#e31e24" stroke-width="2.4"><rect x="24" y="4" width="62" height="44"/><path d="M58 16h20M58 24h20M58 32h14"/><circle cx="20" cy="30" r="8"/><path d="M4 72V54c0-8 8-12 16-12s12 4 14 8l14-10 4 4-18 16v12"/><path d="M30 14l10 10M40 14L30 24"/></svg>
    <div style="margin-top:22px">Training (Rrants<br>and Report Writing)</div>
  </div>
  <a class="btn" href="#" style="left:521px;top:2655px;width:157px;height:39px">View More</a>
</section>

<h2 class="section-title" style="top:2766px">Testimonials</h2>

<article class="testimonial" style="left:81px">
  <div class="avatar" role="img" aria-label="Portrait photograph of Marcus Hale"></div>
  <div class="name">Marcus Hale</div>
  <div class="role">Creative Director</div>
  <p class="quote">Lorem Ipsum simply dummy text the printing and ypesetting simply dummy Ipsum is simply dummy text of the printing.</p>
  <div class="stars">★★★★★</div>
</article>
<article class="testimonial" style="left:436px">
  <div class="avatar" style="background:linear-gradient(135deg,#c84a3c,#e6c9ad)" role="img" aria-label="Portrait photograph of Elena Brooks"></div>
  <div class="name">Elena Brooks</div>
  <div class="role">Creative Director</div>
  <p class="quote">Lorem Ipsum simply dummy text the printing and ypesetting simply dummy Ipsum is simply dummy text of the printing.</p>
  <div class="stars">★★★★★</div>
</article>
<div class="feature-photo" role="img" aria-label="Photograph of a joyful woman in a wheelchair raising her arm outdoors">
  <p>Everyone<br>Benefits<br><b>When Everyone<br>Can Read</b></p>
</div>
<div class="abs serif" style="left:793px;top:3186px;width:326px;text-align:center;font-size:21px">Disabilities</div>
<div class="dots" style="left:405px;top:3207px"><span class="on"></span><span></span><span></span></div>

<section class="contact">
  <h2 class="section-title" style="top:3268px">Contact us</h2>
  <div class="field" style="left:275px;top:3338px;width:316px;height:41px">Name*</div>
  <div class="field" style="left:275px;top:3394px;width:316px;height:41px">Phone*</div>
  <div class="field" style="left:275px;top:3452px;width:316px;height:40px">Email*</div>
  <div class="field message" style="left:604px;top:3338px;width:315px;height:154px">Message</div>
  <a class="btn" href="#" style="left:515px;top:3515px;width:157px;height:39px">Send</a>
</section>

<footer class="site-footer">
  <div class="abs serif" style="left:81px;top:92px;font-size:20px;font-weight:700;display:flex;gap:10px;align-items:center"><span style="width:24px;height:24px;border:2px solid #fff"></span>Crest Drafting Partners</div>
  <p class="txt" style="left:81px;top:149px;width:240px">Lorem Ipsum is simply dummy text the printing and typesetting Ads and in the industry.</p>
  <div class="txt" style="left:79px;top:228px;display:flex;gap:5px;align-items:center">Read More..
    <svg width="14" height="14" viewBox="0 0 14 14" aria-hidden="true"><circle cx="7" cy="7" r="6" fill="none" stroke="#fff"/><path d="M5.5 4l3 3-3 3" fill="none" stroke="#fff"/></svg></div>

  <h4 style="left:390px;top:80px">Quick Link</h4>
  <ul class="quick-links">
    <li>Home</li><li>About us</li><li>Services</li><li>Testimonials</li><li>Contact us</li>
  </ul>

  <h4 style="left:579px;top:80px">Quick Contact</h4>
  <div class="contact-row" style="top:125px"><svg viewBox="0 0 14 14" aria-hidden="true"><path d="M7 13s-4.5-4.6-4.5-7.5a4.5 4.5 0 019 0C11.5 8.4 7 13 7 13z" fill="none" stroke="#fff"/><circle cx="7" cy="5.5" r="1.6" fill="none" stroke="#fff"/></svg>48 Harbour Lane, Northfield,</div>
  <div class="txt" style="left:605px;top:152px">Westshire 67890,</div>
  <div class="txt" style="left:605px;top:178px">United Kingdom</div>
  <div class="contact-row" style="top:203px"><svg viewBox="0 0 14 14" aria-hidden="true"><path d="M2 4c0-1 1-2 2-2h6c1 0 2 1 2 2v1H9V4H5v1H2zM3 6h8l1 6H2z" fill="none" stroke="#fff"/></svg>(00)-987-6612</div>
  <div class="contact-row" style="top:230px"><svg viewBox="0 0 14 14" aria-hidden="true"><rect x="1.5" y="3" width="11" height="8" fill="none" stroke="#fff"/><path d="M1.5 3L7 8l5.5-5" fill="none" stroke="#fff"/></svg>hello@crestdrafting.example</div>

  <h4 style="left:837px;top:80px">Join Our Newleter</h4>
  <p class="txt" style="left:835px;top:124px">Lorem Ipsum is simply dummy&nbsp; the printing.</p>
  <div class="news-input">Email Here</div>
  <a class="btn" href="#" style="left:835px;top:208px;width:284px;height:36px;border-radius:18px">Subscribe</a>
</footer>

<p class="copyright">CopyRight © 2019, Crest Drafting Partners. All Right Reserve</p>
<span class="social red" style="left:938px" aria-label="Social link"></span>
<span class="social" style="left:977px" aria-label="Social link"></span>
<span class="social" style="left:1016px" aria-label="Social link"></span>
<span class="social" style="left:1055px" aria-label="Social link"></span>
<span class="social" style="left:1094px" aria-label="Social link"></span>

</body>
</html>
```